Redesign of page from emergency manual

Please redesign this PDF to look better. Please don't include any stock photos. It must be legible. Making some words bold is probably a good idea.

Here are some things I like :

https://tarrowbooks.com.au/collections/frontpage/products/the-plk-v2-ebook

https://img-cd.vostramediafiles.com/qa-ejkwPLOTYY_SuCKbZNu411Qwgjv8YssPxEdzXN93hDkSRjLXK8WmfgbmrJW4ZZ3yUPK=w1052-h592-rw

```html
<!DOCTYPE html>
<html lang="en">
<head>
<meta charset="utf-8">
<title>Hypertension Acute – Emergency Manual Page</title>
<link href="https://fonts.googleapis.com/css2?family=Montserrat:wght@400;500;600;700;800&display=swap" rel="stylesheet">
<style>
  :root {
    --sky: #5bbde8;
    --navy: #0a66ae;
    --ink-blue: #0d5ea8;
    --text: #1d1d1f;
    --caution-red: #e0141e;
    --caution-bg: #dcedf9;
    --row-yellow: #fdf9d9;
    --backdrop: #e9ebee;
    --white: #ffffff;
  }
  * { box-sizing: border-box; margin: 0; padding: 0; }
  html, body { width: 1200px; height: 614px; overflow: hidden; }
  body {
    background: var(--backdrop);
    font-family: "Montserrat", Arial, sans-serif;
    color: var(--text);
    position: relative;
  }
  .page {
    position: absolute;
    left: 391px; top: 11px;
    width: 836px; height: 1183px;
    background: var(--white);
    transform: scale(0.5);
    transform-origin: top left;
    box-shadow: 0 6px 30px rgba(0,0,0,.18);
    overflow: hidden;
  }
  .header {
    position: absolute; left: 0; top: 0; width: 836px; height: 218px;
    background: var(--sky); color: var(--white);
  }
  .header h1 {
    position: absolute; left: 35px; top: 44px;
    font-size: 63px; font-weight: 800; letter-spacing: 0.3px; line-height: 1;
    white-space: nowrap;
  }
  .header .subtitle {
    position: absolute; left: 39px; top: 133px;
    font-size: 28px; font-weight: 500; line-height: 38px;
  }
  .revision-ribbon { position: absolute; right: 0; top: 0; width: 120px; height: 120px; }
  .intro {
    position: absolute; left: 35px; top: 270px; width: 380px;
    font-size: 15.5px; line-height: 22px;
  }
  .intro .lead { position: relative; padding-left: 19px; }
  .intro .lead::before, .arrow-list li::before {
    content: ""; position: absolute; left: 0; top: 5px;
    border-left: 10px solid var(--navy);
    border-top: 6px solid transparent; border-bottom: 6px solid transparent;
  }
  .intro .checks { list-style: none; margin: 18px 0 0 19px; }
  .intro .checks li {
    color: var(--ink-blue); font-weight: 600; padding-left: 11px; text-indent: -11px;
    margin-bottom: 11px;
  }
  .intro .note { margin: 15px 0 0 19px; font-size: 13px; }
  .bp-table {
    position: absolute; left: 430px; top: 277px; width: 370px;
    border-collapse: collapse; font-size: 17px; text-align: center;
    border: 2px solid var(--navy);
  }
  .bp-table caption {
    background: var(--navy); color: var(--white); font-weight: 600;
    height: 41px; line-height: 41px; font-size: 17px;
  }
  .bp-table th {
    background: var(--sky); color: var(--white); font-weight: 600;
    height: 42px; border-left: 2px solid var(--white);
  }
  .bp-table th:first-child { border-left: none; }
  .bp-table td { height: 38px; border-top: 1.5px solid var(--navy); border-left: 1.5px solid var(--navy); font-weight: 500; }
  .bp-table td:first-child { border-left: none; }
  .bp-table tr.alt td { background: var(--row-yellow); }
  .caution {
    position: absolute; left: 41px; top: 518px; width: 756px; height: 94px;
    background: var(--caution-bg); padding: 15px 13px 0 13px;
    font-size: 15px; line-height: 20.5px; text-align: justify;
  }
  .caution strong { color: var(--caution-red); font-weight: 700; }
  .drug-table {
    position: absolute; left: 42px; top: 633px; width: 751px;
    border-collapse: collapse; border: 2px solid var(--navy);
    font-size: 15.5px; line-height: 21px;
  }
  .drug-table th {
    background: var(--navy); color: var(--white); font-weight: 600; font-size: 17px;
    height: 40px; text-align: center;
  }
  .drug-table td {
    border-top: 1.5px solid var(--navy); vertical-align: top; padding: 12px 10px 0 24px;
  }
  .drug-table td.action { width: 239px; font-weight: 600; border-right: 1.5px solid var(--navy); }
  .drug-table tr.alt td { background: var(--row-yellow); }
  .drug-table tr.r1 td { height: 71px; }
  .drug-table tr.r2 td { height: 105px; }
  .drug-table tr.r3 td { height: 74px; }
  .drug-table tr.r4 td { height: 52px; }
  .arrow-list { list-style: none; }
  .arrow-list li { position: relative; padding-left: 23px; white-space: nowrap; }
  .arrow-list li::before { border-left-color: var(--caution-red); border-left-width: 8px; border-top-width: 5px; border-bottom-width: 5px; top: 5px; }
  .drug-list li.gap { margin-top: 8px; }
  .differential-title {
    position: absolute; left: 43px; top: 996px; width: 750px;
    display: flex; align-items: center; gap: 22px;
    color: var(--navy); font-size: 22px; font-weight: 800; letter-spacing: 0.5px;
  }
  .differential-title::before, .differential-title::after {
    content: ""; flex: 1; height: 2.5px; background: var(--navy);
  }
  .differential { position: absolute; top: 1038px; font-size: 15px; line-height: 20px; }
  .differential li { margin-bottom: 4px; }
  .differential li.spaced { margin-bottom: 9px; }
  .col-a { left: 55px; width: 235px; }
  .col-b { left: 320px; width: 245px; }
  .col-c { left: 595px; width: 200px; }
</style>
</head>
<body>
  <article class="page">
    <header class="header">
      <h1>Hypertension Acute</h1>
      <p class="subtitle">Sustained high blood pressure refractory<br>to treating reversible causes</p>
      <svg class="revision-ribbon" viewBox="0 0 120 120" aria-label="Revision Feb 2020">
        <polygon points="0,0 40,0 120,80 120,120" fill="#0a66ae"/>
        <g transform="translate(72,44) rotate(45)" fill="#fff" font-family="Montserrat, Arial, sans-serif" font-size="11" text-anchor="middle" font-weight="500">
          <text y="-5">REVISION</text>
          <text y="9">FEB 2020</text>
        </g>
      </svg>
    </header>

    <section class="intro">
      <p class="lead">In pediatrics, hypertension is almost always treated by addressing likely causes such as light anesthesia or measurement error:</p>
      <ul class="checks">
        <li>• Ensure correct BP cuff size: cuff bladder width ~ 40% of limb circumference</li>
        <li>• Ensure arterial line transducer is at level of heart</li>
      </ul>
      <p class="note">- Consider placing arterial line if not already present</p>
    </section>

    <table class="bp-table">
      <caption>Hypertensive Blood Pressure Range*</caption>
      <thead><tr><th>Age (yr)</th><th>Systolic</th><th>Diastolic</th></tr></thead>
      <tbody>
        <tr><td>Newborn</td><td>&gt;97</td><td>&gt;70</td></tr>
        <tr class="alt"><td>1-3</td><td>&gt;105</td><td>&gt;61</td></tr>
        <tr><td>4-12</td><td>&gt;113</td><td>&gt;86</td></tr>
      </tbody>
    </table>

    <p class="caution"><strong>CAUTION:</strong> Anti-hypertensive drugs are almost never needed for routine pediatric cases. These medications are used almost exclusively for specialized cardiac, neurosurgical, or endocrine (pheochromocytoma) cases. Consult an expert before use. Rule-out increased ICP.</p>

    <table class="drug-table">
      <thead><tr><th>Action</th><th>Drug (IV Dosing)</th></tr></thead>
      <tbody>
        <tr class="r1"><td class="action">Direct smooth muscle<br>relaxation</td>
          <td><ul class="arrow-list drug-list"><li>Sodium nitroprusside 0.5-10 MICROgrams/kg/min</li><li>HydrALAZINE 0.1-0.2 mg/kg (adult dose 5-10 mg)</li></ul></td></tr>
        <tr class="r2 alt"><td class="action">β-Adrenergic<br>blockade</td>
          <td><ul class="arrow-list drug-list"><li>Esmolol 100-500 MICROgrams/kg over 5 min, then<br>25-300 MICROgrams/kg/min</li><li class="gap">Labetalol (also a effect) 0.2-1 mg/kg q 10 min;<br>0.4-3 mg/kg/hour (infusion)</li></ul></td></tr>
        <tr class="r3"><td class="action">Calcium channel<br>blockade</td>
          <td><ul class="arrow-list drug-list"><li>niCARdapine 0.5-5 MICROgrams/kg/min</li><li class="gap">Clevidipine 0.5-3.5 MICROgrams/kg/min</li></ul></td></tr>
        <tr class="r4 alt"><td class="action">D1-dopamine agonist</td>
          <td><ul class="arrow-list drug-list"><li>Fenoldopam 0.2-0.8 MICROgrams/kg/min</li></ul></td></tr>
      </tbody>
    </table>

    <h2 class="differential-title">CONSIDER DIFFERENTIAL (PARTIAL)</h2>
    <ul class="arrow-list differential col-a">
      <li class="spaced">Light anesthesia (consider<br>vaporizer or infusion pump<br>empty or malfunctioning)</li>
      <li>Hypercarbia</li>
    </ul>
    <ul class="arrow-list differential col-b">
      <li>Hypoxemia</li>
      <li>Arterial line transducer too<br>low or BP cuff too small</li>
      <li>Withdrawal (EtOH or opioid)</li>
    </ul>
    <ul class="arrow-list differential col-c">
      <li>Thyroid Storm</li>
      <li>Pheochromocytoma</li>
      <li>Drug Error</li>
    </ul>
  </article>
</body>
</html>
```